New Business Card Design Project

We want a modern business card that catches the attention of other remodeling companies as well as homeowners. We would like it to be informative but still simple.

Target Market(s)

Residential and other Business's

Contact Information for Business Card

TidyKraft
Phone number is 5152947718
Address is
4817 SW 3rd Lane
Des Moines, Iowa 50313
email is tidykraftia@mailorbit.net

Requirements
Must have
• Our tagline
• Honest | Professional | Affordable

```html
<!DOCTYPE html>
<html lang="en">
<head>
<meta charset="utf-8">
<title>TidyKraft Business Card</title>
<link rel="stylesheet" href="https://fonts.googleapis.com/css2?family=Outfit:wght@500;700&family=Oswald:wght@500&display=swap">
<style>
  :root {
    --charcoal: #434142;
    --brand-blue: #355fb5;
    --brand-orange: #e0541f;
    --paper: #ffffff;
    --canvas: #ffffff;
  }
  * { box-sizing: border-box; margin: 0; padding: 0; }
  html, body {
    width: 1200px; height: 1200px; overflow: hidden;
    background: var(--canvas);
  }
  .card {
    position: absolute;
    left: 220px; width: 760px; height: 456px;
    box-shadow: 8px 8px 10px rgba(0,0,0,0.35);
  }
  .card-front {
    top: 115px;
    background: var(--charcoal);
    border-left: 9px solid var(--brand-blue);
    border-bottom: 8px solid var(--brand-blue);
  }
  .card-back {
    top: 628px;
    background: var(--paper);
  }
  .brand-name {
    position: absolute; left: 0; right: 0;
    text-align: center;
    font-family: "Outfit", sans-serif;
    font-weight: 700;
    text-transform: uppercase;
    letter-spacing: 1px;
    line-height: 1;
  }
  .card-front .brand-name {
    top: 171px; font-size: 106px; color: var(--paper);
    margin-left: -9px;
  }
  .card-back .brand-name {
    top: 88px; font-size: 67px; color: var(--brand-blue);
  }
  .tagline {
    position: absolute; left: 0; right: 0;
    text-align: center;
    font-family: "Oswald", sans-serif;
    font-weight: 500;
    text-transform: uppercase;
    line-height: 1;
  }
  .tagline .divider { display: inline-block; margin: 0 7px; }
  .card-front .tagline {
    top: 278px; font-size: 31px; color: var(--paper); letter-spacing: 1px;
    margin-left: -9px;
  }
  .card-front .tagline .divider { color: var(--brand-blue); }
  .card-back .tagline {
    top: 156px; font-size: 20px; color: var(--brand-blue); letter-spacing: 0.5px;
  }
  .card-back .tagline .divider { color: var(--brand-orange); margin: 0 4px; }
  .mission {
    position: absolute; left: 0; right: 0; top: 214px;
    text-align: center;
    font-family: "Outfit", sans-serif;
    font-weight: 500;
    font-size: 20px;
    line-height: 28.5px;
    color: var(--brand-orange);
    padding-left: 12px;
  }
  .contact {
    position: absolute;
    font-family: "Outfit", sans-serif;
    font-weight: 500;
    font-size: 22.5px;
    line-height: 34px;
    color: var(--brand-blue);
  }
  .contact-address { left: 128px; top: 343px; }
  .contact-direct { left: 470px; top: 343px; }
  .contact-line { position: relative; display: block; white-space: nowrap; }
  .contact-icon { position: absolute; fill: var(--brand-orange); }
  .contact-address .contact-icon { left: -35px; top: 7px; }
  .contact-direct .contact-icon { left: -33px; top: 6px; }
</style>
</head>
<body>
  <section class="card card-front">
    <div class="brand-name">TidyKraft</div>
    <div class="tagline">Honest<span class="divider">|</span>Professional<span class="divider">|</span>Affordable</div>
  </section>

  <section class="card card-back">
    <div class="brand-name">TidyKraft</div>
    <div class="tagline">Honest<span class="divider">|</span>Professional<span class="divider">|</span>Affordable</div>
    <p class="mission">At TidyKraft we feel<br>honesty professionalism and affordability<br>are the backbone of a positive Customer experience</p>

    <div class="contact contact-address">
      <span class="contact-line">
        <svg class="contact-icon" width="22" height="26" viewBox="0 0 22 26" aria-hidden="true">
          <path d="M11 0C5 0 0.5 4.5 0.5 10.3 0.5 17 11 26 11 26S21.5 17 21.5 10.3C21.5 4.5 17 0 11 0ZM11 14.3A4.2 4.2 0 1 1 11 5.9 4.2 4.2 0 0 1 11 14.3Z"/>
        </svg>4817 SW 3rd Lane</span>
      <span class="contact-line">Des Moines,Iowa 50313</span>
    </div>

    <div class="contact contact-direct">
      <span class="contact-line">
        <svg class="contact-icon" width="22" height="22" viewBox="0 0 24 24" aria-hidden="true">
          <path d="M6.6 10.8c1.4 2.8 3.8 5.1 6.6 6.6l2.2-2.2c.3-.3.7-.4 1-.2 1.1.4 2.3.6 3.6.6.6 0 1 .4 1 1V20c0 .6-.4 1-1 1C10.6 21 3 13.4 3 4c0-.6.4-1 1-1h3.5c.6 0 1 .4 1 1 0 1.3.2 2.5.6 3.6.1.3 0 .7-.2 1L6.6 10.8Z"/>
        </svg>515 294 7718</span>
      <span class="contact-line">
        <svg class="contact-icon" width="22" height="16" viewBox="0 0 22 16" aria-hidden="true" style="top:11px">
          <path d="M0 0H22V16H0ZM2 2.5V14H20V2.5L11 9.5Z M2.5 2H19.5L11 8.3Z" fill-rule="evenodd"/>
        </svg>tidykraftia@mailorbit.net</span>
    </div>
  </section>
</body>
</html>
```